Business Card for a Jewellery Brand

Business card for an upscale jewellery brand. Attached is the brand logo and icon and color board. I am looking for two card versions: one for the founder and one is generic. The card should be elegant and convey upscale and premium feel. I am open to both square and rectangle card shapes.

Industry/Entity Type

Jewelry

Contact Information for Business Card

Two cards: (1) Suneha Parmeshwar (Founder) (2) General
(1) Suneha Parmeshwar card should have Name: Suneha Parmeshwar, Title: Founder Email id: suneha@quelm.com.au. Phone no: +61452190437
(2) Generic card should have Email id: info@quelm.com.au. Phone no: +61431267508

Requirements
Must have
• Workmark
• ICON
• Phone no
• Email ID
• ABN: 48291175034 (Note: ABN is Business number in Australia)
• Website: www.quelm.com.au
• Instagram: quelm_jewellery
• Facebook: @quelmjewellery
Nice to have
• Tagline

```html
<!DOCTYPE html>
<html lang="en">
<head>
<meta charset="utf-8">
<title>QUELM Business Cards</title>
<link rel="stylesheet" href="https://fonts.googleapis.com/css2?family=Roboto:wght@400&display=swap">
<style>
  :root {
    --backdrop: #5b5c5e;
    --card: #231f20;
    --rose: #dba59b;
    --ink: #ffffff;
  }
  * { margin: 0; padding: 0; box-sizing: border-box; }
  html, body {
    width: 1200px;
    height: 1200px;
    overflow: hidden;
    background: var(--backdrop);
    font-family: "Roboto", Arial, sans-serif;
  }
  .canvas { position: relative; width: 1200px; height: 1200px; }
  .card {
    position: absolute;
    left: 180px;
    width: 840px;
    height: 500px;
    background: var(--card);
  }
  .card--founder { top: 80px; }
  .card--general { top: 620px; }

  .brand-mark {
    position: absolute;
    left: 50%;
    border-radius: 50%;
    transform: translateX(-50%);
  }
  .card--founder .brand-mark {
    top: 70px;
    width: 74px;
    height: 74px;
    border: 4px solid var(--rose);
  }
  .card--general .brand-mark {
    top: 110px;
    width: 170px;
    height: 170px;
    border: 10px solid var(--ink);
  }

  .wordmark {
    position: absolute;
    left: 0;
    right: 0;
    text-align: center;
    color: var(--rose);
    letter-spacing: 0.32em;
    text-indent: 0.32em;
    line-height: 1;
  }
  .card--founder .wordmark { top: 168px; font-size: 54px; }
  .card--general .wordmark { top: 312px; font-size: 48px; color: var(--ink); }

  .person {
    position: absolute;
    top: 262px;
    left: 0;
    right: 0;
    text-align: center;
  }
  .person__name { font-size: 28px; color: var(--rose); line-height: 1.2; }
  .person__title { font-size: 20px; color: var(--ink); line-height: 1.4; }

  .divider {
    position: absolute;
    top: 350px;
    left: 32px;
    right: 32px;
    height: 3px;
    background: var(--rose);
  }
  .contacts {
    position: absolute;
    top: 368px;
    list-style: none;
    color: var(--ink);
    font-size: 20px;
  }
  .contacts--primary { left: 32px; }
  .contacts--social { left: 262px; }
  .contacts li {
    display: flex;
    align-items: center;
    gap: 9px;
    height: 34px;
  }
  .contacts svg { width: 16px; height: 16px; flex: none; }
  .social-dot {
    width: 14px;
    height: 14px;
    flex: none;
    background: var(--rose);
    border-radius: 3px;
  }
  .address {
    position: absolute;
    top: 372px;
    right: 32px;
    text-align: right;
    color: var(--ink);
    font-size: 20px;
    line-height: 30px;
  }
  .address__label { color: var(--rose); }

  .general-contact {
    position: absolute;
    left: 0;
    right: 0;
    bottom: 44px;
    text-align: center;
    color: var(--ink);
    font-size: 18px;
  }
  .general-contact span + span::before {
    content: "·";
    color: var(--rose);
    margin: 0 14px;
  }
</style>
</head>
<body>
<main class="canvas">
  <section class="card card--founder">
    <div class="brand-mark"></div>
    <div class="wordmark">QUELM</div>
    <div class="person">
      <p class="person__name">Suneha Parmeshwar</p>
      <p class="person__title">Founder</p>
    </div>
    <div class="divider"></div>

    <ul class="contacts contacts--primary">
      <li>
        <svg viewBox="0 0 24 24" aria-hidden="true"><path fill="#dba59b" d="M6.6 10.8a15.1 15.1 0 0 0 6.6 6.6l2.2-2.2c.3-.3.7-.4 1-.2 1.1.4 2.3.6 3.6.6.6 0 1 .4 1 1V20c0 .6-.4 1-1 1A17 17 0 0 1 3 4c0-.6.4-1 1-1h3.5c.6 0 1 .4 1 1 0 1.3.2 2.5.6 3.6.1.3 0 .7-.2 1z"/></svg>
        <span>+61452190437</span>
      </li>
      <li><span class="social-dot"></span><span>quelm_jewellery</span></li>
      <li>
        <svg viewBox="0 0 24 24" aria-hidden="true"><g fill="none" stroke="#dba59b" stroke-width="2"><circle cx="12" cy="12" r="9"/><ellipse cx="12" cy="12" rx="4" ry="9"/><path d="M3 12h18M5 7h14M5 17h14"/></g></svg>
        <span>www.quelm.com.au</span>
      </li>
    </ul>

    <ul class="contacts contacts--social">
      <li>
        <svg viewBox="0 0 24 24" aria-hidden="true"><path fill="#dba59b" d="M2 5h20v14H2z"/><path fill="none" stroke="#231f20" stroke-width="1.8" d="M2.5 5.5 12 13l9.5-7.5"/></svg>
        <span>suneha@quelm.com.au</span>
      </li>
      <li><span class="social-dot"></span><span>@quelmjewellery</span></li>
    </ul>

    <div class="address">
      <p class="address__label">Address</p>
      <p>Suite 1400, 228 Harlow Street</p>
      <p>Fenwick NSW 2093</p>
      <p>ABN 48291175034</p>
    </div>
  </section>

  <section class="card card--general">
    <div class="brand-mark"></div>
    <div class="wordmark">QUELM</div>
    <p class="general-contact">
      <span>info@quelm.com.au</span><span>+61431267508</span><span>ABN 48291175034</span>
    </p>
  </section>
</main>
</body>
</html>
```